Powerpoint design for european B2B business

We need a Powerpoint design for a newly established IT company with a B2B focus. We want to develop management information systems that help managers communicate goals into their organization and analyze their organizational activities and performance.

We defined the attached color scale, please relate your design to these colors.

The design should be simple and straight, serious and professional and leave enough space for the content ... :-)

Target Market(s)

B2B, companies larger than 200 employees

Industry/Entity Type

Business

Font styles to use
Sans Serif

Requirements
Should not have
• too playful design, clipart style

```html
<!DOCTYPE html>
<html lang="en">
<head>
<meta charset="UTF-8">
<title>Pages of Content</title>
<link href="https://fonts.googleapis.com/css2?family=Jost:wght@400;600&display=swap" rel="stylesheet">
<style>
  :root {
    --stage: #c8c8c8;
    --paper: #ffffff;
    --navy: #245073;
    --sage: #8bbf9e;
    --rule: #e6e8ea;
    --index: #c3c8cd;
    --band-text: #3d6689;
  }
  * { margin: 0; padding: 0; box-sizing: border-box; }
  html, body {
    width: 1200px; height: 1039px; overflow: hidden;
    background: var(--stage);
    font-family: "Jost", "Century Gothic", sans-serif;
  }
  .slide {
    position: absolute; left: 134px; top: 158px;
    width: 967px; height: 725px;
    background: var(--paper);
  }
  .page-tab {
    position: absolute; left: 802px; top: 0;
    width: 116px; height: 97px;
    background: var(--sage);
    color: var(--navy);
    font-size: 17px;
    display: flex; align-items: center; justify-content: center;
  }
  .side-band {
    position: absolute; left: 802px; top: 102px;
    width: 116px; height: 623px;
    background: var(--navy);
    overflow: hidden;
  }
  .side-band .web {
    position: absolute; left: 88px; bottom: 30px;
    transform-origin: left bottom;
    transform: rotate(-90deg);
    white-space: nowrap;
    color: var(--band-text);
    font-size: 41px; letter-spacing: 1px;
    line-height: 1;
  }
  .title {
    position: absolute; left: 47px; top: 70px;
    font-size: 50px; font-weight: 400;
    color: var(--navy); letter-spacing: 0.5px;
  }
  .title strong { color: var(--sage); font-weight: 600; }
  .contents {
    position: absolute; left: 47px; top: 190px;
    width: 642px; list-style: none;
  }
  .contents li {
    height: 67.5px;
    display: flex; align-items: center;
    border-bottom: 1.5px solid var(--rule);
    font-size: 19.5px; color: var(--navy);
    letter-spacing: 0.4px;
  }
  .contents li:last-child { border-bottom: none; }
  .contents .num { width: 43px; color: var(--index); }
  .contents .dot { width: 24px; font-size: 14px; }
  .contents li.shift .dot { margin-left: -6px; }
  .brand {
    position: absolute; left: 55px; top: 648px;
    font-size: 30px; font-weight: 600;
    color: var(--navy); letter-spacing: -0.5px;
  }
</style>
</head>
<body>
  <section class="slide">
    <h1 class="title">PAGES OF <strong>CONTENT</strong></h1>
    <ol class="contents">
      <li><span class="num">01</span><span class="dot">•</span>ABOUT OUR COMPANY</li>
      <li><span class="num">02</span><span class="dot">•</span>OUR SERVICES</li>
      <li><span class="num">03</span><span class="dot">•</span>OUR MISSION</li>
      <li><span class="num">04</span><span class="dot">•</span>WHAT WE DO?</li>
      <li><span class="num">05</span><span class="dot">•</span>OUR MISSION</li>
      <li class="shift"><span class="num">06</span><span class="dot">•</span>WHAT WE DO?</li>
    </ol>
    <div class="brand">Norvalis</div>
    <div class="page-tab">Page 1</div>
    <div class="side-band"><span class="web">www.norvalis.com</span></div>
  </section>
</body>
</html>
```